NEW Gym Timetable for Muay Thai gym!

We need a new timetable for our Muay Thai gym - the times, classes and logos are attached. Our primary logo font is MACHINE BT

The gym is called Kroval Fit. The address is Level 2, 58-60 Brindlemere Road, Tallowdene, Canberra

We are open Monday to Saturday and Sunday by appointment.

Our website and more information can be found at www.kroval.com.au.

Please message me for more information/feedback

```html
<!DOCTYPE html>
<html lang="en">
<head>
<meta charset="utf-8">
<title>Kroval Fit – Class Timetable</title>
<link rel="stylesheet" href="https://fonts.googleapis.com/css2?family=Alfa+Slab+One&family=Roboto:ital,wght@0,300;0,400;0,700;0,900;1,900&display=swap">
<style>
  :root {
    --green-light: #0f6a35;
    --green-dark: #0b4a26;
    --brand-green: #0c5c2e;
    --line: rgba(255,255,255,0.12);
    --white: #ffffff;
    --black: #0a0a0a;
    --band: #222222;
  }
  * { box-sizing: border-box; margin: 0; padding: 0; }
  html, body { width: 927px; height: 1200px; overflow: hidden; background: var(--black); }
  .poster { position: relative; width: 927px; height: 1200px; overflow: hidden; font-family: 'Roboto', sans-serif; color: var(--white); }

  .header { position: absolute; left: 0; top: 0; width: 927px; height: 426px; }
  .header-texture {
    position: absolute; inset: 0 0 76px 0;
    background: radial-gradient(ellipse 300px 260px at 50% 30%, #f4f4f4 0%, #c9c9c9 35%, #6d6d6d 70%, #3a3a3a 100%);
  }
  .header-band { position: absolute; left: 0; right: 0; top: 350px; height: 76px; background: var(--band); border-bottom: 2px solid #3a3a3a; }
  .brand-name {
    position: absolute; left: 0; right: 0; top: 70px; text-align: center;
    font-family: 'Alfa Slab One', serif; font-size: 76px; letter-spacing: 4px;
    color: var(--brand-green); text-transform: uppercase;
  }
  .brand-mark { position: absolute; left: 373px; top: 200px; width: 180px; height: 180px; background: var(--brand-green); }

  .stripes { position: absolute; top: 426px; left: 0; width: 927px; height: 712px; display: grid; grid-template-columns: 142px 196px 198px 195px 196px; }
  .stripe-light { background: var(--green-light); }
  .stripe-dark { background: var(--green-dark); }

  .timetable {
    position: absolute; top: 426px; left: 0; width: 927px; height: 712px;
    display: grid;
    grid-template-columns: 142px 196px 198px 195px 196px;
    grid-template-rows: 124px 108px 96px 101px 100px 100px 83px;
  }
  .row { display: contents; --pad: 29px; }
  .row-mo { --pad: 29px; }
  .row-tu { --pad: 16px; }
  .row-we { --pad: 12px; }
  .row-th { --pad: 27px; }
  .row-fr { --pad: 18px; }
  .row-sa { --pad: 26px; }

  .day, .session, .slot-empty, .appointment { border-bottom: 1px solid var(--line); overflow: hidden; }
  .day {
    display: flex; align-items: center; padding-left: 48px;
    font-family: 'Alfa Slab One', serif; font-size: 40px; font-variant: small-caps; line-height: 1;
  }
  .session { display: flex; flex-direction: column; align-items: center; justify-content: flex-start; padding-top: var(--pad); text-align: center; }
  .time { font-weight: 400; font-size: 18px; line-height: 22px; }
  .time small { font-size: 14px; }
  .class-name { font-weight: 700; font-size: 17px; line-height: 27px; text-transform: uppercase; letter-spacing: 0.3px; }
  .class-name.stacked { line-height: 21px; margin-top: 3px; }
  .note { font-weight: 400; font-size: 12px; line-height: 16px; margin-top: 2px; letter-spacing: 0.3px; }
  .slot-empty { display: flex; align-items: center; justify-content: center; }
  .slot-mark { width: 58px; height: 66px; background: rgba(255,255,255,0.14); }
  .appointment {
    grid-column: 2 / 6; display: flex; align-items: center; justify-content: center; gap: 12px;
    font-style: italic; font-weight: 900; text-transform: uppercase;
  }
  .appointment .lead { font-size: 36px; letter-spacing: 1px; }
  .appointment .tail { font-size: 27px; }

  .footer {
    position: absolute; left: 0; top: 1138px; width: 927px; height: 62px; background: var(--black);
    display: flex; align-items: center; justify-content: center;
    color: var(--green-light); font-weight: 900; font-style: italic; font-size: 29px; letter-spacing: 0.5px;
  }
</style>
</head>
<body>
<div class="poster">
  <header class="header">
    <div class="header-texture" role="img" aria-label="Dark grunge wall texture lit by a central spotlight"></div>
    <div class="header-band"></div>
    <div class="brand-name">Kroval Fit</div>
    <div class="brand-mark"></div>
  </header>

  <div class="stripes" aria-hidden="true">
    <div class="stripe-light"></div><div class="stripe-dark"></div><div class="stripe-light"></div><div class="stripe-dark"></div><div class="stripe-light"></div>
  </div>

  <main class="timetable">
    <div class="row row-mo">
      <div class="day">Mo</div>
      <div class="session"><span class="time">6:00<small>AM</small> - 7:00<small>AM</small></span><span class="class-name">Clinching</span><span class="note">(FIGHTERS/BY INVITATION)</span></div>
      <div class="session"><span class="time">5:30<small>PM</small> - 6:30<small>PM</small></span><span class="class-name">Muay Thai</span></div>
      <div class="session"><span class="time">6:30<small>PM</small> - 7:30<small>PM</small></span><span class="class-name">Padwork &amp;<br>Bagwork</span></div>
      <div class="session"><span class="time">7:30<small>PM</small> - 8:30<small>PM</small></span><span class="class-name">Fighters</span></div>
    </div>

    <div class="row row-tu">
      <div class="day">Tu</div>
      <div class="session"><span class="time">6:00<small>AM</small> - 7:00<small>AM</small></span><span class="class-name">Muay HIIT</span></div>
      <div class="session"><span class="time">5:30<small>PM</small> - 6:30<small>PM</small></span><span class="class-name">Boxing</span></div>
      <div class="session"><span class="time">6:30<small>PM</small> - 7:30<small>PM</small></span><span class="class-name">Muay HIIT</span></div>
      <div class="session"><span class="time">7:30<small>PM</small> - 8:30<small>PM</small></span><span class="class-name">Fighters</span></div>
    </div>

    <div class="row row-we">
      <div class="day">We</div>
      <div class="session"><span class="time">6:00<small>AM</small> - 7:00<small>AM</small></span><span class="class-name">Clinching</span><span class="note">(FIGHTERS/BY INVITATION)</span></div>
      <div class="session"><span class="time">5:30<small>PM</small> - 6:30<small>PM</small></span><span class="class-name">Muay Thai</span></div>
      <div class="session"><span class="time">6:30<small>PM</small> - 7:30<small>PM</small></span><span class="class-name">Padwork &amp;<br>Bagwork</span></div>
      <div class="session"><span class="time">7:30<small>PM</small> - 8:30<small>PM</small></span><span class="class-name">Fighters</span></div>
    </div>

    <div class="row row-th">
      <div class="day">Th</div>
      <div class="session"><span class="time">6:00<small>AM</small> - 7:00<small>AM</small></span><span class="class-name">Muay HIIT</span></div>
      <div class="session"><span class="time">5:30<small>PM</small> - 6:30<small>PM</small></span><span class="class-name">Boxing</span></div>
      <div class="session"><span class="time">6:30<small>PM</small> - 7:30<small>PM</small></span><span class="class-name">Muay HIIT</span></div>
      <div class="session"><span class="time">7:30<small>PM</small> - 8:30<small>PM</small></span><span class="class-name">Fighters</span></div>
    </div>

    <div class="row row-fr">
      <div class="day">Fr</div>
      <div class="slot-empty"><div class="slot-mark"></div></div>
      <div class="session"><span class="time">5:30<small>PM</small> - 6:30<small>PM</small></span><span class="class-name stacked">Muay HIIT<br>Weekly Wrap</span></div>
      <div class="slot-empty"><div class="slot-mark"></div></div>
      <div class="slot-empty"><div class="slot-mark"></div></div>
    </div>

    <div class="row row-sa">
      <div class="day">Sa</div>
      <div class="session"><span class="time">8:00<small>AM</small> - 8:45<small>AM</small></span><span class="class-name">Muay HIIT</span></div>
      <div class="session"><span class="time">9:00<small>PM</small> - 11:00<small>PM</small></span><span class="class-name">Sparring</span></div>
      <div class="session"><span class="time">12:00<small>PM</small> - 1:00<small>PM</small></span><span class="class-name">Muay HIIT</span></div>
      <div class="slot-empty"><div class="slot-mark"></div></div>
    </div>

    <div class="row row-su">
      <div class="day">Su</div>
      <div class="appointment"><span class="lead">Personal Training</span><span class="tail">by Appointment</span></div>
    </div>
  </main>

  <footer class="footer">FOR MORE INFO CONTACT US</footer>
</div>
</body>
</html>
```